KV Holding ltd*

I need a full website designed for for a 10,000m2 strorage facity which specialize in heavy commercial storage

it needs to be in english please

Target Market(s)

Comercial sector

Industry/Entity Type

Construction Company

Logo Text

KV

Coding

Coded - Design and coding required

Number of Pages Required

1 page

Font styles to use
Sans Serif

Colors
ec1f27
ffffff

Requirements
Must have
• Tel 0064 218846097
• email- lewis@kvholding.co.nz
Nice to have
• We specilize in large items with the facilty have 3 15tonne Gantry cranes and heavy mobile lifting equipment we can store items up to 20 tonne and we are fully covered and secure.
• square meter rates from 20m2 to 10,000 m2

```html
<!DOCTYPE html>
<html lang="en">
<head>
<meta charset="utf-8">
<title>KV Storage – Heavy Commercial Storage</title>
<link href="https://fonts.googleapis.com/css2?family=Bangers&family=Lato:wght@400;700&family=Montserrat:wght@400;500;600&display=swap" rel="stylesheet">
<style>
:root{
  --red:#ec1f27;
  --red-dark:#c8141b;
  --white:#ffffff;
  --ink:#2b2b2b;
  --muted:#7a7a7a;
  --charcoal:#3b3e44;
  --dark:#1e1f22;
  --gold:#d9c33a;
  --light:#f1f2f4;
}
*{box-sizing:border-box;margin:0;padding:0}
html,body{width:1200px;height:4286px;overflow:hidden}
body{position:relative;background:var(--white);font-family:"Lato",sans-serif;color:var(--muted)}
.abs{position:absolute}
.display{font-family:"Bangers",sans-serif;letter-spacing:1px}
.brand{font-family:"Montserrat",sans-serif;font-weight:600;color:var(--red);letter-spacing:4px;display:flex;align-items:center;gap:10px}
.brand .dot{width:34px;height:34px;border-radius:50%;background:var(--red)}

/* header */
.topbar{top:0;left:0;width:1200px;height:125px;background:var(--white)}
.contact-line{font-family:"Lato",sans-serif;font-size:14px;color:var(--muted);display:flex;align-items:center;gap:8px}
.socials{display:flex;gap:10px}
.socials span{width:26px;height:26px;border-radius:50%;background:var(--red);display:block}
.nav{top:73px;left:80px;width:1040px;height:40px;display:flex;font-family:"Montserrat",sans-serif;font-size:14px;letter-spacing:2px;color:#555}
.nav a{flex:1;display:flex;align-items:center;justify-content:center;text-decoration:none;color:inherit}
.nav a.active{background:#4d5055;color:var(--gold)}

/* hero */
.hero{top:125px;left:0;width:1200px;height:740px;overflow:hidden;background:linear-gradient(90deg,#111 45%,#6a6a6a 100%)}
.hero-photo{left:0;top:0;width:560px;height:740px;background:linear-gradient(180deg,#9aa 0%,#c8285a 30%,#b0204a 60%,#777 100%);clip-path:ellipse(100% 120% at 0% 50%)}
.hero-kicker{top:205px;left:560px;width:610px;text-align:center;font-family:"Montserrat",sans-serif;font-size:14px;letter-spacing:4px;color:var(--white)}
.hero-title{top:248px;left:560px;width:610px;text-align:center;font-size:38px;line-height:56px;color:var(--white)}
.booking{top:394px;left:629px;width:471px;height:100px;border:2px solid var(--gold);padding:8px}
.booking .fields{display:flex;gap:8px}
.booking .field{flex:1;height:36px;border:1px solid var(--gold);font-size:12px;color:var(--gold);padding:10px 12px}
.booking .submit{margin-top:8px;height:38px;border:1px solid var(--gold);display:flex;align-items:center;justify-content:center;font-family:"Montserrat",sans-serif;font-size:20px;letter-spacing:3px;color:var(--gold)}
.btn{background:var(--red);color:var(--white);font-family:"Montserrat",sans-serif;font-size:13px;display:flex;align-items:center;justify-content:center;gap:8px;border-radius:3px}
.btn i{width:14px;height:14px;border-radius:50%;background:var(--white);display:block}
.hero-btn{width:234px;height:45px;top:541px}

/* titles */
.red-title{background:linear-gradient(180deg,var(--red),var(--red-dark));color:var(--white);display:flex;align-items:center;justify-content:center;font-size:40px;box-shadow:0 3px 6px rgba(0,0,0,.25)}
.para{font-size:13.4px;line-height:24px;color:var(--muted)}

/* about */
.about-photo{top:870px;left:115px;width:444px;height:694px;background:linear-gradient(160deg,#6a6a6a,#8e4a3a 60%,#3a2a26)}
.feature h4{font-family:"Bangers",sans-serif;font-size:22px;color:#333;font-weight:400;letter-spacing:1px}
.feature .ico{width:44px;height:44px;border-radius:50%;background:var(--red)}
.feature p{font-size:13.4px;line-height:24px}

/* services */
.svc-photo{width:238px;height:158px}
.svc-title{font-family:"Bangers",sans-serif;font-size:22px;color:#333;letter-spacing:1px}
.tile{background:linear-gradient(180deg,#7a7a7a,#4a4a4a);color:var(--white);font-size:13px;display:flex;flex-direction:column;align-items:center;justify-content:flex-end;padding-bottom:14px;text-align:center;line-height:20px}
.tile .ring{width:62px;height:62px;border:3px solid var(--white);border-radius:50%;margin-bottom:10px}

/* why */
.why-label{font-family:"Montserrat",sans-serif;font-weight:600;font-size:9px;line-height:10px;color:#333}

/* testimonials */
.testi-bg{top:3378px;left:0;width:1200px;height:480px;background:linear-gradient(180deg,#ffffff,#e3e5e8 40%,#d9dce0)}
.card{top:3544px;width:331px;height:220px;background:var(--white);text-align:center;padding:26px 26px 0;font-size:13px;line-height:25px;color:var(--muted)}
.card.dark{background:#4c4f55;color:var(--white)}
.who{display:flex;align-items:center;justify-content:center;gap:12px;margin-top:22px;text-align:left}
.who .avatar{width:58px;height:58px;border-radius:50%;background:#9aa0a8}
.who b{display:block;font-family:"Montserrat",sans-serif;font-weight:500;font-size:15px;color:#333;line-height:20px}
.card.dark .who b{color:var(--white)}
.who small{font-size:10px;letter-spacing:1px;line-height:14px}

/* footer */
.footer{top:3810px;left:0;width:1200px;height:476px;background:linear-gradient(180deg,#45484e,#1c1d20);clip-path:polygon(0 100px,600px 0,1200px 100px,1200px 476px,0 476px)}
.footer .para{color:var(--white)}
.search{top:3982px;left:453px;width:304px;height:42px;display:flex}
.search .box{flex:1;background:var(--white);font-size:12px;color:#aaa;padding:14px 14px}
.search .go{width:42px;background:var(--red)}
.f-photo{top:4040px;left:453px;width:304px;height:133px;background:linear-gradient(135deg,#cfd3d8,#3a6fb0 45%,#d8c23a 70%,#444)}
.f-contact{font-size:14px;color:var(--white);display:flex;align-items:center;gap:14px}
.f-contact i{width:16px;height:12px;background:var(--red);display:block}
.f-nav{top:4221px;left:0;width:1200px;display:flex;justify-content:center;gap:6px;font-size:14px;color:var(--white)}
.f-nav span{padding:5px 12px}
.f-nav .active{background:#6e6b55;color:var(--gold)}
</style>
</head>
<body>

<header class="abs topbar">
  <div class="abs brand" style="top:12px;left:80px;font-size:30px"><span class="dot"></span>KV STORAGE</div>
  <div class="abs contact-line" style="top:12px;left:405px">
    <svg width="12" height="16" viewBox="0 0 12 16"><rect x="1" y="0" width="10" height="16" rx="2" fill="#ec1f27"/><rect x="3" y="2" width="6" height="10" fill="#fff"/></svg>0064 2188 46097</div>
  <div class="abs contact-line" style="top:12px;left:655px">
    <svg width="16" height="12" viewBox="0 0 16 12"><rect width="16" height="12" fill="#ec1f27"/><path d="M0 0 L8 7 L16 0" stroke="#fff" fill="none"/></svg>lewis@kvholding.co.nz</div>
  <div class="abs socials" style="top:9px;left:910px"><span></span><span></span><span></span><span></span><span></span></div>
  <nav class="abs nav">
    <a class="active">HOME</a><a>ABOUT</a><a>SERVICES</a><a>FAQ</a><a>CONTACT</a>
  </nav>
</header>

<section class="abs hero">
  <div class="abs hero-photo" role="img" aria-label="Storage corridor with red roller doors and a forklift carrying a wooden crate"></div>
  <p class="abs hero-kicker">SPECIALIZE IN HEAVY COMMERCIAL STORAGE</p>
  <h1 class="abs hero-title display" style="font-weight:400">WE ARE THE LEADING COMMERCIAL<br>STORAGE PROVIDER</h1>
  <form class="abs booking">
    <div class="fields"><div class="field">Name</div><div class="field">Email</div><div class="field">Phone</div></div>
    <div class="submit">BOOK AN APPOINTMENT</div>
  </form>
  <div class="abs btn hero-btn" style="left:621px"><i></i>&nbsp;&nbsp;LEARN MORE</div>
  <div class="abs btn hero-btn" style="left:874px"><i></i>&nbsp;&nbsp;CONTACT US</div>
</section>

<section>
  <div class="abs about-photo" role="img" aria-label="Hand holding a tablet showing warehouse forklift operations"></div>
  <h2 class="abs red-title display" style="top:884px;left:617px;width:505px;height:75px;font-weight:400">ABOUT KV STORAGE</h2>
  <p class="abs para" style="top:982px;left:639px;width:484px">Lorem ipsum dolor sit amet, consectetur adipiscing elit, sed do eiusmod tempor incididunt ut labore et dolore magna aliqua. Orci dapibus ultrices in iaculis. Tortor dignissim convallis aenean et tortor at risus. Faucibus nisl tincidunt eget nullam non nisi est. Diam sollicitudin tempor id eu nisl nunc mi ipsum faucibus. Vestibulum rhoncus est pellentesque elit ullamcorper dignissim. Scelerisque eleifend donec pretium vulputate sapien nec sagittis aliquam. Ornare arcu odio ut sem nulla pharetra diam sit. Id diam vel quam elementum pulvinar etiam. Sapien eget mi proin sed libero enim sed faucibus turpis. Metus vulputate eu scelerisque felis. Posuere sollicitudin aliquam ultrices sagittis. Sed faucibus turpis in eu mi bibendum. Sapien nec sagittis aliquam malesuada bibendum. Mauris a diam maecenas sed enim ut. Nec sagittis aliquam malesuada bibendum arcu vitae elementum curabitur.</p>
  <div class="abs feature" style="top:1298px;left:620px;width:250px;display:flex;gap:16px">
    <div class="ico"></div>
    <div><h4>OUR MISSION</h4><p>Lorem ipsum dolor sit amet, consectetur adipiscing elit. Ut elit tellus, luctus nec ullamcorper mattis, pulvinar dapibus leo.</p></div>
  </div>
  <div class="abs feature" style="top:1298px;left:878px;width:250px;display:flex;gap:16px">
    <div class="ico"></div>
    <div><h4>OUR VISION</h4><p>Lorem ipsum dolor sit amet, consectetur adipiscing elit. Ut elit tellus, luctus nec ullamcorper mattis, pulvinar dapibus leo.</p></div>
  </div>
  <div class="abs btn" style="top:1458px;left:963px;width:164px;height:43px"><i></i>LEARN MORE</div>
</section>

<section>
  <h2 class="abs red-title display" style="top:1651px;left:301px;width:604px;height:66px;font-weight:400">HOW WE HELP YOU</h2>
  <p class="abs para" style="top:1742px;left:80px;width:1047px">Lorem ipsum dolor sit amet, consectetur adipiscing elit, sed do eiusmod tempor incididunt ut labore et dolore magna aliqua. Orci dapibus ultrices in iaculis. Tortor dignissim convallis aenean et tortor at risus. Faucibus nisl tincidunt eget nullam non nisi est. Diam sollicitudin tempor id eu nisl nunc mi ipsum faucibus. Vestibulum rhoncus est pellentesque elit ullamcorper dignissim.</p>

  <div class="abs svc-photo" style="top:1855px;left:80px;background:linear-gradient(180deg,#c9ccd2,#7a8ea8 60%,#b8bcc2)" role="img" aria-label="Large warehouse with racking and pallets"></div>
  <h3 class="abs svc-title" style="top:1860px;left:331px;font-weight:400">COMMERCIAL STORAGE SERVICES</h3>
  <p class="abs para" style="top:1886px;left:331px;width:796px">Lorem ipsum dolor sit amet, consectetur adipiscing elit. Ut elit tellus, luctus nec ullamcorper mattis, pulvinar dapibus leo.Lorem ipsum dolor sit amet, consectetur adipiscing elit, sed do eiusmod tempor incididunt ut labore et dolore magna aliqua. Orci dapibus ultrices in iaculis. Tortor dignissim convallis aenean et tortor at risus. Faucibus nisl tincidunt eget nullam non nisi est. Diam sollicitudin tempor id eu nisl nunc mi ipsum faucibus. Vestibulum rhoncus est pellentesque elit ullamcorper dignissim.</p>

  <div class="abs tile" style="top:2068px;left:115px;width:148px;height:127px"><div class="ring"></div>Heavy Equipment</div>
  <div class="abs tile" style="top:2068px;left:281px;width:148px;height:127px"><div class="ring"></div>Construction</div>
  <div class="abs tile" style="top:2068px;left:446px;width:148px;height:127px"><div class="ring"></div>Offices</div>
  <div class="abs tile" style="top:2068px;left:612px;width:148px;height:127px"><div class="ring"></div>Business</div>
  <div class="abs tile" style="top:2068px;left:777px;width:148px;height:127px"><div class="ring"></div>Retailers</div>
  <div class="abs tile" style="top:2068px;left:943px;width:148px;height:127px"><div class="ring"></div>Hotels</div>

  <div class="abs svc-photo" style="top:2295px;left:80px;background:linear-gradient(180deg,#9a9ea4,#5e6268 60%,#8a8e94)" role="img" aria-label="Person walking down a storage aisle lined with boxes"></div>
  <h3 class="abs svc-title" style="top:2300px;left:331px;font-weight:400">RESIDENTIAL STORAGE SERVICES</h3>
  <p class="abs para" style="top:2326px;left:331px;width:796px">Lorem ipsum dolor sit amet, consectetur adipiscing elit. Ut elit tellus, luctus nec ullamcorper mattis, pulvinar dapibus leo.Lorem ipsum dolor sit amet, consectetur adipiscing elit, sed do eiusmod tempor incididunt ut labore et dolore magna aliqua. Orci dapibus ultrices in iaculis. Tortor dignissim convallis aenean et tortor at risus. Faucibus nisl tincidunt eget nullam non nisi est. Diam sollicitudin tempor id eu nisl nunc mi ipsum faucibus. Vestibulum rhoncus est pellentesque elit ullamcorper dignissim.</p>

  <div class="abs tile" style="top:2508px;left:115px;width:181px;height:149px"><div class="ring"></div>Household Goods<br>Storage</div>
  <div class="abs tile" style="top:2508px;left:314px;width:181px;height:149px;padding-bottom:34px"><div class="ring"></div>Car &amp; Truck Storage</div>
  <div class="abs tile" style="top:2508px;left:513px;width:181px;height:149px;padding-bottom:34px;background:linear-gradient(180deg,#7d8fa3,#4d5e70)"><div class="ring"></div>Boat Storage</div>
  <div class="abs tile" style="top:2508px;left:712px;width:181px;height:149px;padding-bottom:34px"><div class="ring"></div>Piano Storage</div>
  <div class="abs tile" style="top:2508px;left:910px;width:181px;height:149px;padding-bottom:34px"><div class="ring"></div>Hotels</div>

  <div class="abs btn" style="top:2696px;left:907px;width:220px;height:43px"><i></i>CHECK OUR SERVICES</div>
</section>

<section>
  <h2 class="abs red-title display" style="top:2917px;left:97px;width:489px;height:67px;font-weight:400">WHY CHOSE US</h2>
  <p class="abs para" style="top:3009px;left:93px;width:496px;text-align:justify">Lorem ipsum dolor sit amet, consectetur adipiscing elit, sed do eiusmod tempor incididunt ut labore et dolore magna aliqua. Orci dapibus ultrices in iaculis. Tortor dignissim convallis aenean et tortor at risus. Faucibus nisl tincidunt eget nullam non nisi est. Diam sollicitudin tempor id eu nisl nunc mi ipsum faucibus. Vestibulum rhoncus est pellentesque elit ullamcorper dignissim.Lorem ipsum dolor sit amet, consectetur adipiscing elit, sed do eiusmod tempor incididunt ut labore et dolore magna aliqua. Orci dapibus ultrices in iaculis. Tortor dignissim convallis aenean et tortor at risus. Faucibus nisl tincidunt eget nullam non nisi est. Diam sollicitudin tempor id eu nisl nunc mi ipsum faucibus. Vestibulum rhoncus est pellentesque elit ullamcorper dignissim.</p>
  <div class="abs btn" style="top:3290px;left:93px;width:163px;height:43px"><i></i>LEARN MORE</div>

  <svg class="abs" style="top:2950px;left:660px" width="400" height="360" viewBox="0 0 400 360">
    <path d="M180 12 A166 166 0 0 1 180 344" fill="none" stroke="#555" stroke-width="2"/>
    <circle cx="114" cy="178" r="98" fill="#ec1f27"/>
    <circle cx="114" cy="178" r="80" fill="#1e1f22"/>
    <text x="114" y="188" text-anchor="middle" font-family="Montserrat, sans-serif" font-weight="600" font-size="16" fill="#ec1f27" letter-spacing="2">KV STORAGE</text>
    <g fill="#fff" stroke="#ec1f27" stroke-width="3">
      <circle cx="185" cy="30" r="18"/><circle cx="265" cy="100" r="18"/><circle cx="282" cy="180" r="18"/><circle cx="265" cy="260" r="18"/><circle cx="185" cy="330" r="18"/>
    </g>
    <g fill="#ec1f27"><circle cx="185" cy="30" r="7"/><circle cx="265" cy="100" r="7"/><circle cx="282" cy="180" r="7"/><circle cx="265" cy="260" r="7"/><circle cx="185" cy="330" r="7"/></g>
  </svg>
  <div class="abs why-label" style="top:2961px;left:878px">PROFESSIONAL<br>AND TRAINED<br>EMPLOYEES</div>
  <div class="abs why-label" style="top:3031px;left:962px">WE HAVE HEAVY<br>MOBILE LIFTING<br>EQUIPMENT</div>
  <div class="abs why-label" style="top:3115px;left:978px">WE ARE FULLY<br>COVERED &amp;<br>SECURE</div>
  <div class="abs why-label" style="top:3200px;left:958px">NO HIDDEN<br>FEES</div>
  <div class="abs why-label" style="top:3273px;left:878px">WE CAN STORE<br>ITEMS UP TO<br>20 TONNE</div>
</section>

<section>
  <div class="abs testi-bg"></div>
  <h2 class="abs red-title display" style="top:3446px;left:301px;width:604px;height:67px;font-weight:400">WHAT OUR CLIENTS SAY</h2>
  <div class="abs card" style="left:88px">Click edit button to change this text. Lorem ipsum dolor sit amet, consectetur adipiscing elit. Ut elit tellus, luctus nec ullamcorper mattis, pulvinar dapibus leo.
    <div class="who"><div class="avatar" role="img" aria-label="Client portrait"></div><div><b>Mara Tolland</b><small>CEO NORTHWAY</small></div></div></div>
  <div class="abs card dark" style="left:438px">Click edit button to change this text. Lorem ipsum dolor sit amet, consectetur adipiscing elit. Ut elit tellus, luctus nec ullamcorper mattis, pulvinar dapibus leo.
    <div class="who"><div class="avatar" role="img" aria-label="Client portrait"></div><div><b>Nina Harrow</b><small>CEO NORTHWAY</small></div></div></div>
  <div class="abs card" style="left:787px">Click edit button to change this text. Lorem ipsum dolor sit amet, consectetur adipiscing elit. Ut elit tellus, luctus nec ullamcorper mattis, pulvinar dapibus leo.
    <div class="who"><div class="avatar" role="img" aria-label="Client portrait"></div><div><b>Owen Pryde</b><small>CEO NORTHWAY</small></div></div></div>
</section>

<footer class="abs footer"></footer>
<div class="abs brand" style="top:3986px;left:115px;font-size:32px"><span class="dot"></span>KV STORAGE</div>
<p class="abs para" style="top:4048px;left:115px;width:305px;color:#fff;font-size:13.4px">Lorem ipsum dolor sit amet, consectetur adipiscing elit, sed do eiusmod tempor incididunt ut labore et dolore magna aliqua.</p>
<div class="abs search"><div class="box">Search...</div><div class="go"></div></div>
<div class="abs f-photo" role="img" aria-label="Forklift moving stacked goods in a warehouse"></div>
<div class="abs" style="top:3986px;left:789px;font-family:Montserrat,sans-serif;font-weight:600;font-size:14px;color:#fff">GET IN TOUCH</div>
<div class="abs f-contact" style="top:4048px;left:789px"><i></i>lewis@kvholding.co.nz</div>
<div class="abs f-contact" style="top:4091px;left:789px"><i></i>0064 2188 46097</div>
<div class="abs socials" style="top:4131px;left:789px;gap:14px"><span></span><span></span><span></span><span></span><span></span></div>
<nav class="abs f-nav"><span class="active">Home</span><span>About</span><span>Services</span><span>FAQ</span><span>Contact</span></nav>

</body>
</html>
```